New Website Deisgn. Guaranteed Project.

I would like a site similar to this: http://givebikeforhope.org.

old site: http://wheelsforrelief.org

Create a professional website; a car donation site seeking leads to return calls.

Please see http://givebikeforhope.org for the concept I am after.

The webpage should have a professional feel. The pages to include are 'Home', 'About us' and 'Get Started'

Industry/Entity Type

It Professional

Coding

Coded - Design and coding required

Number of Pages Required

1 page

```html
<!DOCTYPE html>
<html lang="en">
<head>
<meta charset="utf-8">
<title>Bright Path Kids Foundation – Car Donation</title>
<link href="https://fonts.googleapis.com/css2?family=Open+Sans:wght@400;600&family=Varela+Round&display=swap" rel="stylesheet">
<style>
:root{
  --teal:#0e9a96;
  --teal-dark:#0a6f6c;
  --orange:#ffa400;
  --orange-light:#ffc21a;
  --field:#ffb733;
  --ink:#333;
  --muted:#777;
  --line:#c9c9c9;
  --white:#fff;
}
*{box-sizing:border-box;margin:0;padding:0}
html,body{width:710px;height:1200px;overflow:hidden}
body{position:relative;font-family:"Open Sans",sans-serif;color:var(--ink);background:var(--white)}
.abs{position:absolute}
h1,h2,h3,.round{font-family:"Varela Round",sans-serif;font-weight:400}

/* header */
.brand{left:70px;top:12px;display:flex;align-items:center;gap:8px}
.brand-mark{width:36px;height:36px;background:var(--orange);border-radius:4px}
.brand-name{font-family:"Open Sans",sans-serif;font-size:12.5px;line-height:11px;color:var(--teal-dark);width:80px}
.social{right:75px;top:32px;display:flex;gap:4px}
.social span{width:20px;height:20px;border-radius:50%;background:var(--teal)}

/* nav */
.nav{left:0;top:62px;width:710px;height:30px;background:linear-gradient(var(--teal),var(--teal-dark))}
.nav ul{list-style:none;display:flex;margin-left:70px;height:30px}
.nav li{color:var(--white);font-size:9.5px;font-weight:600;line-height:30px;padding:0 13px}
.nav li.active{background:#07504e}

/* hero */
.hero{left:0;top:92px;width:641px;height:260px;background:linear-gradient(90deg,#c4c6c8 0%,#e6e7e8 35%,#d9b89a 55%,#8bc34a 62%,#e4e4e4 80%)}
.hero-title{left:68px;top:172px;font-size:19.5px;line-height:21px;color:var(--teal)}
.hero-title span{color:var(--orange)}
.hero-text{left:70px;top:223px;width:190px;font-size:8px;line-height:12px;color:#555}
.dots{left:71px;top:257px;display:flex;gap:6px}
.dots i{width:9px;height:9px;border-radius:50%;background:#888}
.dots i:first-child{background:none;border:1.5px solid #888}

/* form */
.quote{left:435px;top:63px;width:206px;height:289px;background:linear-gradient(var(--orange-light),var(--orange) 30%)}
.quote-call{text-align:center;color:var(--white);font-size:11px;margin-top:11px}
.quote-phone{text-align:center;color:var(--white);font-size:17px;font-weight:600}
.quote-label{text-align:center;color:#fff3d6;font-size:9px;margin-top:16px}
.field{position:absolute;height:19px;background:var(--field);color:var(--white);font-size:7.5px;line-height:19px;padding-left:8px}
.field.select::after{content:"⌄";position:absolute;right:8px;top:-3px;font-size:10px}
.quote-btn{position:absolute;left:15px;top:237px;width:176px;height:28px;background:linear-gradient(#4a4a4a,#1e1e1e);color:var(--white);font-size:11px;text-align:center;line-height:28px;font-weight:600}

/* steps */
.step{width:157px;height:157px;border:1.5px solid var(--line);border-radius:50%;text-align:center;top:366px}
.step svg{display:block;margin:21px auto 6px}
.step h3{font-size:12px;line-height:14px;color:#222}
.step p{font-size:7px;line-height:12px;color:var(--muted);margin-top:6px}
.step-arrow{top:415px}
.divider{left:0;top:551px;width:710px;height:1px;background:#ddd}

/* why */
.why{left:0;top:552px;width:710px;height:291px;background:radial-gradient(ellipse at 55% 40%,#f2e9e5 0%,#f7f5f4 50%,#fbfbfb 100%)}
.why-title{left:0;top:576px;width:710px;text-align:center;font-size:16.5px;color:#333}
.why-text{left:125px;top:603px;width:470px;text-align:center;font-size:7.5px;line-height:12px;color:#888}
.feature{width:210px}
.feature h3{font-size:12px;line-height:12px;color:var(--teal)}
.feature p{font-size:7px;line-height:12px;color:#666;margin-top:4px}
.feature-icon{position:absolute}

/* faq */
.faq{left:0;top:843px;width:710px;height:278px;background:linear-gradient(120deg,var(--teal) 0%,#9fb43a 55%,#ffb400 100%)}
.faq-title{left:0;top:873px;width:710px;text-align:center;color:var(--white);font-size:16px}
.faq-item{left:131px;width:449px;height:26px;border:1px solid rgba(255,255,255,.8);color:var(--white);font-size:8.5px;line-height:24px;padding-left:13px}
.faq-item::after{content:"";position:absolute;right:12px;top:8px;width:6px;height:6px;border-left:1.3px solid #fff;border-top:1.3px solid #fff;transform:rotate(45deg)}
.faq-item.open::after{transform:rotate(225deg);top:5px}
.faq-answer{left:131px;top:932px;width:449px;height:51px;background:rgba(90,90,20,.35);color:var(--white);font-size:7px;line-height:12px;padding:13px 30px 0 25px}
.faq-answer b{position:absolute;left:14px;top:19px;font-weight:400;font-size:8px}

/* footer */
.footer-nav{left:0;top:1147px;width:710px;display:flex;justify-content:center;gap:20px;font-size:10px;color:#333}
.copyright{left:0;top:1168px;width:710px;text-align:center;font-size:7.5px;color:#555}
</style>
</head>
<body>

<header>
  <div class="abs brand"><span class="brand-mark"></span><span class="brand-name">Bright Path Kids Foundation</span></div>
  <div class="abs social"><span></span><span></span><span></span><span></span></div>
</header>

<nav class="abs nav">
  <ul><li class="active">HOME</li><li>ABOUT US</li><li>HOW IT WORKS</li><li>FAQ</li><li>WHY US</li></ul>
</nav>

<section>
  <div class="abs hero" role="img" aria-label="Photo of a smiling boy making a heart with his hands beside a silver car"></div>
  <h1 class="abs hero-title">Donate Your Old Car<br><span>and Get Tax Deduction</span></h1>
  <p class="abs hero-text">In ullamcorper est eget tempor cursus neque mi consectetuer mi a ultricies massa</p>
  <div class="abs dots"><i></i><i></i><i></i><i></i></div>

  <form class="abs quote">
    <p class="quote-call">CALL TOLL-FREE</p>
    <p class="quote-phone">1-800-555-0142</p>
    <p class="quote-label">Donation Pick Up Form</p>
    <div class="field" style="left:15px;top:84px;width:86px">First Name</div>
    <div class="field" style="left:105px;top:84px;width:86px">Last Name</div>
    <div class="field" style="left:15px;top:109px;width:176px">Zip Code</div>
    <div class="field" style="left:15px;top:133px;width:176px">Email address</div>
    <div class="field" style="left:15px;top:157px;width:176px">Day Phone</div>
    <div class="field select" style="left:15px;top:182px;width:86px">Year of Vehicle</div>
    <div class="field select" style="left:105px;top:182px;width:86px">Make of Vehicle</div>
    <div class="field select" style="left:15px;top:207px;width:176px">Model of Vehicle</div>
    <div class="quote-btn">Get a Quote Now</div>
  </form>
</section>

<section>
  <div class="abs step" style="left:78px">
    <svg width="32" height="40" viewBox="0 0 32 40"><path d="M2 1h20l8 8v30H2z" fill="none" stroke="#0e9a96" stroke-width="2"/><path d="M7 14h18M7 19h18M7 24h18M7 29h18M7 34h18" stroke="#0e9a96" stroke-width="2"/></svg>
    <h3>Fill Our Quote<br>Form Now</h3>
    <p>Praesent elementum elit at tellus<br>nec ultricies sit am</p>
  </div>
  <svg class="abs step-arrow" style="left:236px" width="40" height="16" viewBox="0 0 40 16"><path d="M1 6Q20 0 36 12" fill="none" stroke="#f08a24" stroke-dasharray="2 2"/><path d="M33 8l4 5-6 0z" fill="#f08a24"/></svg>
  <div class="abs step" style="left:280px">
    <svg width="48" height="40" viewBox="0 0 48 40"><circle cx="36" cy="11" r="9" fill="#0e9a96"/><path d="M30 17L6 38l-3-3 4-3-2-2 3-2-2-2 18-11z" fill="#0e9a96"/></svg>
    <h3>Donate Your Car<br>to Charity</h3>
    <p>Praesent elementum elit at tellus<br>nec ultricies sit am</p>
  </div>
  <svg class="abs step-arrow" style="left:437px" width="40" height="16" viewBox="0 0 40 16"><path d="M1 6Q20 0 36 12" fill="none" stroke="#f08a24" stroke-dasharray="2 2"/><path d="M33 8l4 5-6 0z" fill="#f08a24"/></svg>
  <div class="abs step" style="left:481px">
    <svg width="34" height="40" viewBox="0 0 34 40"><path d="M4 1h26v36H14" fill="none" stroke="#0e9a96" stroke-width="2"/><circle cx="13" cy="12" r="2.5" fill="none" stroke="#0e9a96" stroke-width="1.5"/><circle cx="21" cy="20" r="2.5" fill="none" stroke="#0e9a96" stroke-width="1.5"/><path d="M22 10L12 22M1 30l5 6 9-12" fill="none" stroke="#0e9a96" stroke-width="2"/></svg>
    <h3>Recieve<br>Tax Deduction</h3>
    <p>Praesent elementum elit at tellus<br>nec ultricies sit am</p>
  </div>
  <div class="abs divider"></div>
</section>

<section>
  <div class="abs why" role="img" aria-label="Soft faded photo of a mother and daughter embracing"></div>
  <h2 class="abs why-title">Why Choose Us</h2>
  <p class="abs why-text">Integer congue augue et malesuada iaculis ipsum dui aliquet felis at cursus magna nisl nec elit Praesent elementum elit at tellus nec ultricies sit amet porttitor mattis enim In massa libero interdum nec interdum vel blandit sed nulla in ullamcor-per est eget tempor cursus neque mi consectetuer mi a ultricies massa est sed nisl</p>

  <svg class="feature-icon" style="left:106px;top:672px" width="20" height="36" viewBox="0 0 20 36"><path d="M3 2h14l-3 8H6z" fill="#ffa400"/><path d="M10 10v10a6 6 0 1 1-6 6" fill="none" stroke="#ffa400" stroke-width="3"/></svg>
  <div class="abs feature" style="left:140px;top:674px"><h3>Free Towing in 24-48 hours</h3><p>We will pick up your car donation when it's most convenient for you either at home or work at no cost to you.</p></div>

  <svg class="feature-icon" style="left:384px;top:674px" width="44" height="26" viewBox="0 0 44 26"><path d="M2 18v-6l8-2 6-8h14l8 8 4 2v6z" fill="#ffa400"/><circle cx="11" cy="19" r="5" fill="#ffa400" stroke="#fff" stroke-width="2"/><circle cx="33" cy="19" r="5" fill="#ffa400" stroke="#fff" stroke-width="2"/></svg>
  <div class="abs feature" style="left:432px;top:674px;width:220px"><h3>We Accept All Cars</h3><p>We accept all cars in any condition and running or not.</p></div>

  <svg class="feature-icon" style="left:104px;top:748px" width="26" height="26" viewBox="0 0 26 26"><circle cx="13" cy="13" r="12" fill="#ffa400"/><path d="M7 6q5 2 4 6t-4 5M16 4q-2 4 2 6t3 6" fill="none" stroke="#fff" stroke-width="2"/></svg>
  <div class="abs feature" style="left:140px;top:748px"><h3>Car Will Be Sold on the Largest Auction Network</h3><p>We will sell your car at the largest resale auction network to get you the highest tax write-off possible.</p></div>

  <svg class="feature-icon" style="left:386px;top:748px" width="40" height="34" viewBox="0 0 40 34"><text x="20" y="18" font-size="20" font-family="Open Sans,sans-serif" font-weight="600" fill="#ffa400">$</text><path d="M2 22h12l6 3h10l8-5v4l-10 8H14l-12-4z" fill="#ffa400"/></svg>
  <div class="abs feature" style="left:432px;top:748px;width:210px"><h3>Hassle Free Donation</h3><p>We can assist with everything: DMV, Smog &amp; IRS paperwork. Just submit your form below and we will take care of every-thing else.</p></div>
</section>

<section>
  <div class="abs faq"></div>
  <h2 class="abs faq-title">Frequently Asked Questions</h2>
  <div class="abs faq-item open" style="top:906px">Q: Donec dictum lectus non odio Cras a ante vitae</div>
  <div class="abs faq-answer"><b>A:</b>Aorttitor mattis enim In massa libero interdum nec interdum vel blandit sed nulla In ullamcorper est eget tempor cursus neque mi consectetuer mi a ultricies massa est sed nisl Class aptent taciti sociosq</div>
  <div class="abs faq-item" style="top:984px">Q: Class aptent taciti sociosqu ad litora torquent per conubia nostra</div>
  <div class="abs faq-item" style="top:1010px">Q: Etiam eu urna Sed porta Suspendisse quam</div>
  <div class="abs faq-item" style="top:1036px">Q: Fusce tellus Sed metus augue convallis et vehicula</div>
  <div class="abs faq-item" style="top:1062px">Q: Praesent vitae lacus Ut velit enim</div>
</section>

<footer>
  <nav class="abs footer-nav"><span>Home</span><span>About us</span><span>Donate Car</span><span>Why Us</span><span>Privacy Policy</span><span>Contact</span></nav>
  <p class="abs copyright">© 2017 Company Name &nbsp;All right reserved &nbsp;Term of Use</p>
</footer>

</body>
</html>
```